Technology Project Portal - Project Listing portal

We require a logo & website designed for our new project.

Project Name: lumafold
Description:
We have a webapp where clients and service providers can come, signup and register development projects. Service providers can the browse projects and contact clients via the portal

Design brief:
Clean & Modern - See Attached color palet & style references. (Feel free to try alternative color palets)

See Project Proposal for site requirements.
UX flow section details pages requires

Examples of all standard UI Components required e.g.
text box / field
Drop down
date picker
etc..

Target Market(s)

Business / Technology providers

Logo Text

LumaFold

Coding

Coded - Design and coding required

Number of Pages Required

5+ page

Requirements
Must have
• Clean Modern Design
Examples for all common UI elements
Templates for common Web App Dialogs e.g. Confirm Delete/Logout etc

```html
<!DOCTYPE html>
<html lang="en">
<head>
<meta charset="utf-8">
<title>Lumafold – Screens</title>
<link rel="stylesheet" href="https://fonts.googleapis.com/css2?family=Poppins:wght@400;500;600&display=swap">
<style>
  :root {
    --brand: #ff3c00;
    --ink: #2b2b2b;
    --muted: #555555;
    --dark: #4a4a4a;
    --tab-dark: #525252;
    --panel-grey: #d6d6d6;
    --field-border: #c9c9c9;
    --page: #ededed;
    --white: #ffffff;
  }
  * { box-sizing: border-box; margin: 0; padding: 0; }
  html, body { width: 1200px; height: 2521px; overflow: hidden; }
  body {
    position: relative;
    background: var(--page);
    font-family: "Poppins", sans-serif;
    color: var(--ink);
  }
  .screen {
    position: absolute;
    left: 233px;
    width: 760px;
    height: 465px;
    background: var(--white);
    box-shadow: 0 2px 10px rgba(0,0,0,0.12);
  }
  .screen--home { top: 230px; }
  .screen--login { top: 1028px; }
  .screen--signup { top: 1853px; }

  .abs { position: absolute; }
  .btn {
    position: absolute;
    display: flex; align-items: center; justify-content: center;
    border-radius: 6px;
    font-weight: 500;
    color: var(--white);
    background: var(--brand);
    font-size: 15px;
  }
  .btn--dark { background: var(--dark); }
  .field {
    position: absolute;
    height: 47px;
    border: 2px solid var(--field-border);
    border-radius: 6px;
    background: var(--white);
    padding-left: 7px;
    display: flex; align-items: center;
    font-size: 15px;
    color: var(--muted);
  }

  /* Home screen */
  .app-bar {
    position: absolute; left: 8px; top: 7px; width: 744px; height: 65px;
    background: var(--brand);
    display: flex; align-items: center;
  }
  .brand-name {
    margin-left: 21px;
    font-size: 27px; font-weight: 600; color: var(--white);
  }
  .app-bar__login {
    left: 641px; top: 12px; width: 94px; height: 43px;
    background: var(--white); color: var(--brand); font-size: 17px;
  }
  .signup-btn { left: 97px; top: 238px; width: 122px; height: 64px; font-size: 20px; border-radius: 8px; }

  .dialog {
    position: absolute; left: 308px; top: 102px; width: 420px; height: 336px;
    background: var(--white);
    box-shadow: 0 0 6px rgba(0,0,0,0.15);
  }
  .dialog__head {
    position: absolute; left: 8px; top: 7px; width: 405px; height: 61px;
    background: var(--panel-grey);
    display: flex; align-items: center; padding-left: 13px;
    font-size: 18px; font-weight: 500;
  }
  .dialog__close { left: 371px; top: 21px; width: 35px; height: 35px; }
  .alert {
    position: absolute; left: 9px; top: 80px; width: 402px; height: 55px;
    background: var(--brand); border-radius: 6px; color: var(--white);
  }
  .alert__icon { left: 10px; top: 10px; width: 35px; height: 35px; }
  .alert__title { left: 60px; top: 7px; font-size: 15px; font-weight: 500; }
  .alert__text { left: 60px; top: 29px; font-size: 13px; }
  .dialog .field { left: 9px; width: 401px; color: var(--ink); }
  .dialog__cancel { left: 9px; top: 272px; width: 88px; height: 45px; }
  .dialog__login { left: 104px; top: 272px; width: 88px; height: 45px; }

  /* Login & signup screens */
  .page-bar {
    position: absolute; left: 8px; top: 7px; width: 744px; height: 66px;
    background: var(--brand); color: var(--white);
    font-size: 30px; font-weight: 500;
    display: flex; align-items: center; padding-left: 14px;
  }
  .panel {
    position: absolute; left: 8px; top: 85px; width: 744px; height: 372px;
    background: var(--white);
    box-shadow: 0 0 5px rgba(0,0,0,0.1);
  }
  .login-form .field { left: 149px; width: 402px; }
  .check {
    position: absolute; left: 150px; width: 23px; height: 23px;
    border: 2px solid var(--field-border); border-radius: 5px;
  }
  .check-label { position: absolute; left: 180px; font-size: 16px; color: var(--ink); }
  .submit-btn { left: 152px; top: 269px; width: 88px; height: 45px; }

  .tabs { position: absolute; left: 8px; top: 7px; width: 744px; height: 65px; display: flex; }
  .tab {
    display: flex; align-items: center; justify-content: center;
    color: var(--white); font-size: 30px; font-weight: 500;
  }
  .tab--client { width: 370px; background: var(--brand); }
  .tab--service { width: 374px; background: var(--tab-dark); }
  .signup-form .field { left: 172px; width: 401px; }
  .next-btn { left: 329px; top: 255px; width: 88px; height: 45px; }
</style>
</head>
<body>

<section class="screen screen--home">
  <header class="app-bar">
    <span class="brand-name">Lumafold</span>
    <span class="btn app-bar__login">LOGIN</span>
  </header>
  <span class="btn signup-btn">SIGNUP</span>

  <div class="dialog">
    <div class="dialog__head">Login</div>
    <svg class="abs dialog__close" viewBox="0 0 35 35" aria-hidden="true">
      <circle cx="17.5" cy="17.5" r="17.5" fill="#444"/>
      <path d="M13 13 L22 22 M22 13 L13 22" stroke="#fff" stroke-width="3" stroke-linecap="round"/>
    </svg>
    <div class="alert">
      <svg class="abs alert__icon" viewBox="0 0 35 35" aria-hidden="true">
        <circle cx="17.5" cy="17.5" r="17.5" fill="#fff"/>
        <path d="M13.5 13.5 L21.5 21.5 M21.5 13.5 L13.5 21.5" stroke="#2b2b2b" stroke-width="3" stroke-linecap="round"/>
      </svg>
      <span class="abs alert__title">Unable to login</span>
      <span class="abs alert__text">bad username/password, access denied</span>
    </div>
    <div class="field" style="top:156px">test</div>
    <div class="field" style="top:213px;font-size:18px;letter-spacing:1px">••••</div>
    <span class="btn dialog__cancel">CANCEL</span>
    <span class="btn btn--dark dialog__login">LOGIN</span>
  </div>
</section>

<section class="screen screen--login">
  <header class="page-bar">Login</header>
  <div class="panel login-form">
    <div class="field" style="top:58px">Enter Your Email</div>
    <div class="field" style="top:115px">Enter Your Pasword</div>
    <span class="check" style="top:179px"></span>
    <span class="check-label" style="top:179px">Remember user logged in for 30 days</span>
    <span class="check" style="top:222px"></span>
    <span class="check-label" style="top:222px">Password reset via email if user needs password reset</span>
    <span class="btn submit-btn">SUBMIT</span>
  </div>
</section>

<section class="screen screen--signup">
  <nav class="tabs">
    <span class="tab tab--client">Client</span>
    <span class="tab tab--service">Service</span>
  </nav>
  <div class="panel signup-form">
    <div class="field" style="top:70px">Name</div>
    <div class="field" style="top:127px">Email</div>
    <div class="field" style="top:187px">Password</div>
    <span class="btn next-btn">NEXT</span>
  </div>
</section>

</body>
</html>
```